When the boots match march on! book cover design

Book cover for a business, non-fiction book.
About stepping up, being who you truly are, and willing not to fit in.

TITLE: When The Boots Match, March On!
SUBTITLE: Quit copying the chief others expect of you and begin shaping the chief nobody else could ever shape...
AUTHOR: Tobias Hartwell-Brenner
Updates

we never uploaded the brief

Target Market(s)

Business people, curious leaders, insiders who have a secret itch to be an outsider
AGE: 35-50 years old

Font styles to use
Sans Serif
Other font styles liked:
• designer's choice!

Requirements
Must have
• Very visual
Imagery must reflect the topic of the book

```html
<!DOCTYPE html>
<html lang="en">
<head>
<meta charset="utf-8">
<title>When The Boots Match, March On! – Cover Spread</title>
<link rel="stylesheet" href="https://fonts.googleapis.com/css2?family=Tinos:wght@400;700&display=swap">
<style>
  :root {
    --backdrop: #67645a;
    --band: #e1ddd2;
    --paper: #ffffff;
    --ink: #140c0c;
    --accent-red: #d0242a;
    --rule: #3c3a36;
    --photo-grey: #939598;
    --body-ink: #3a3a3a;
  }
  * { margin: 0; padding: 0; box-sizing: border-box; }
  html, body {
    width: 813px; height: 1200px; overflow: hidden;
    background: var(--backdrop);
  }
  .canvas { position: relative; width: 813px; height: 1200px; }
  .spread {
    position: absolute; left: 35px; top: 326px;
    width: 742px; height: 548px;
    background: var(--paper);
    border: 1px solid var(--rule);
    font-family: "Tinos", "Times New Roman", serif;
    color: var(--ink);
    overflow: hidden;
  }
  .title-band {
    position: absolute; left: 0; top: 0; width: 100%; height: 166px;
    background: var(--band);
  }
  .panel { position: absolute; top: 0; height: 100%; }
  .back { left: 0; width: 354px; }
  .spine {
    left: 354px; width: 33px;
    border-left: 1px solid var(--rule); border-right: 1px solid var(--rule);
  }
  .front { left: 387px; width: 355px; }

  /* Each condensed line is centred on its panel independently of its unscaled width */
  .line {
    display: block; position: relative; left: 50%;
    width: max-content; white-space: nowrap;
  }

  .title {
    position: absolute; left: 0; width: 100%;
    font-weight: 700; letter-spacing: -0.01em;
  }
  .title .line { transform: translateX(-50%) scaleX(0.78); }
  .back .title { top: 58px; font-size: 33px; line-height: 1.05; }
  .front .title { top: 44px; font-size: 42px; line-height: 1.08; }
  .front .title .line { transform: translateX(-50%) scaleX(0.74); }

  .author-photo {
    position: absolute; left: 55px; top: 184px; width: 80px; height: 104px;
    background: var(--photo-grey);
  }
  .blurb {
    position: absolute; font-size: 7.3px; line-height: 9.7px;
    color: var(--body-ink); text-align: justify; hyphens: auto;
  }
  .blurb-lead { left: 147px; top: 183px; width: 158px; }
  .blurb-mid { left: 55px; top: 297px; width: 250px; }
  .blurb-end { left: 55px; top: 366px; width: 250px; }
  .code-box {
    position: absolute; left: 185px; top: 449px; width: 120px; height: 47px;
    border: 1px solid var(--ink); background: var(--paper);
  }

  .spine-text {
    position: absolute; left: 50%; white-space: nowrap;
    font-weight: 700; font-size: 16px;
    transform-origin: 0 0;
  }
  .spine-text span { display: inline-block; transform: scaleX(0.82); transform-origin: 0 50%; }
  .spine-title { top: 84px; transform: rotate(90deg) translateY(-50%); }
  .spine-author { top: 326px; transform: rotate(90deg) translateY(-50%); }

  .cover-art {
    position: absolute; left: 95px; top: 214px; width: 165px; height: 162px;
  }
  .subtitle {
    position: absolute; left: 0; top: 380px; width: 100%;
    color: var(--accent-red);
    font-weight: 700; font-size: 18.5px; line-height: 21.5px;
  }
  .subtitle .line { transform: translateX(-50%) scaleX(0.86); }
  .author {
    position: absolute; left: 0; top: 497px; width: 100%;
    font-weight: 700; font-size: 20px;
  }
  .author .line { transform: translateX(-50%) scaleX(0.88); }
</style>
</head>
<body>
<main class="canvas">
  <section class="spread">
    <div class="title-band"></div>

    <div class="panel back">
      <h2 class="title"><span class="line">When The Boots Match,</span><span class="line">March On!</span></h2>
      <div class="author-photo" role="img" aria-label="Author portrait placeholder"></div>
      <p class="blurb blurb-lead">Lorem ipsum dolor sit amet, consectetur adipiscing elit. Mauris congue orci vitae sapien auctor, et laoreet tellus egestas. Donec suscipit porta dui sed tempor. Class aptent taciti sociosqu ad litora torquent per conubia nostra, per inceptos himenaeos. Fusce non turpis sit amet nunc laoreet pharetra. Integer eu diam in metus posuere malesuada. Maecenas pharetra risus a nulla varius, ac dignissim felis egestas. Curabitur bibendum lectus vel diam facilisis sodales.</p>
      <p class="blurb blurb-mid">Sed molestie dui vel mollis pulvinar. Ut ac mi sem. Duis elementum massa metus, ac tempor nisl malesuada sit amet. Fusce auctor feugiat sapien sit amet dignissim. Maecenas sit amet semper neque. Donec sodales, augue vel interdum posuere, justo leo auctor eros, sed vulputate felis felis non ipsum. Cras sit amet consequat mauris. Sed ex metus, rutrum vitae vulputate et, elementum sed sapien.</p>
      <p class="blurb blurb-end">Vestibulum vel odio vel arcu efficitur cursus id in augue. Donec eu pharetra erat, at aliquet magna. Morbi scelerisque viverra venenatis. Curabitur justo massa, aliquam eu dolor a, egestas vehicula libero. Nunc consequat tincidunt neque sed porttitor. Curabitur in aliquet mauris. Vivamus at viverra eros. Vivamus est est, aliquam sed tempor at,</p>
      <div class="code-box"></div>
    </div>

    <div class="panel spine">
      <div class="spine-text spine-title"><span>When The Boots Match, March On!</span></div>
      <div class="spine-text spine-author"><span>Tobias Hartwell-Brenner</span></div>
    </div>

    <div class="panel front">
      <h1 class="title"><span class="line">When The Boots Match,</span><span class="line">March On!</span></h1>
      <svg class="cover-art" viewBox="0 0 165 162" role="img" aria-label="Illustration: a red jigsaw piece wearing a navy cap, lifted above its empty white slot">
        <defs>
          <radialGradient id="art-tone" cx="45%" cy="45%" r="65%">
            <stop offset="0" stop-color="#cf2a2e"/>
            <stop offset="0.55" stop-color="#e4c6c6"/>
            <stop offset="1" stop-color="#ffffff"/>
          </radialGradient>
        </defs>
        <rect width="165" height="162" fill="url(#art-tone)"/>
      </svg>
      <p class="subtitle"><span class="line">Quit copying the chief</span><span class="line">others expect of you</span><span class="line">and begin shaping the chief</span><span class="line">nobody else could ever shape...</span></p>
      <p class="author"><span class="line">Tobias Hartwell-Brenner</span></p>
    </div>
  </section>
</main>
</body>
</html>
```